Private Investigation Business Card Design

I need a business card for a new private investigation company named Veltrane Inquiries. I perform mainly surveillance jobs, vehicle repossessions, document serves etc. The final design should aim for a professional look. The logo has a magnifying glass with stick man arms and legs and is in a running action to show the "Veltrane" aspect of the name. If the colour scheme could remain the same as the website www.veltraneinquiries.com.au with silvers,blacks and a couple electric blue highlights.
Business
Contact Information for Business Card
Morgan Kalvane
Veltrane Inquiries
0437862914
PO Box 48, Birchwood NSW 2301
info@veltraneinquiries.com.au
www.veltraneinquiries.com.au

```html
<!DOCTYPE html>
<html lang="en">
<head>
<meta charset="UTF-8">
<title>Veltrane Inquiries – Business Card</title>
<link rel="stylesheet" href="https://fonts.googleapis.com/css2?family=Montserrat:wght@400;500;600;700&display=swap">
<style>
  :root {
    --backdrop: #e7e8ea;
    --card: #ffffff;
    --ink: #3a3a3a;
    --ink-soft: #555555;
    --rule: #5a5a5a;
    --silver: #8a8d91;
    --shadow: rgba(0, 0, 0, 0.18);
  }
  * { box-sizing: border-box; margin: 0; padding: 0; }
  html, body {
    width: 1200px;
    height: 800px;
    overflow: hidden;
    background: var(--backdrop);
    font-family: "Montserrat", sans-serif;
    color: var(--ink);
  }
  .stage {
    width: 1200px;
    height: 800px;
    display: flex;
    align-items: center;
    justify-content: center;
    gap: 60px;
  }
  .card {
    position: relative;
    width: 500px;
    height: 286px;
    background: var(--card);
    box-shadow: 0 6px 18px var(--shadow);
  }

  /* Front */
  .card-front {
    display: flex;
    align-items: center;
    justify-content: center;
  }
  .brand {
    display: flex;
    align-items: center;
    gap: 14px;
  }
  .brand-name {
    color: var(--silver);
    font-size: 32px;
    font-weight: 600;
    line-height: 1;
    white-space: nowrap;
  }
  .brand-dot {
    width: 26px;
    height: 26px;
    border-radius: 50%;
    background: var(--silver);
  }

  /* Back */
  .details-frame {
    position: absolute;
    inset: 0;
  }
  .details-frame line,
  .details-frame rect {
    stroke: var(--rule);
    stroke-width: 1;
    fill: none;
  }
  .detail {
    position: absolute;
    display: flex;
    align-items: center;
    justify-content: center;
    text-align: center;
  }
  .person-name {
    left: 80px; top: 30px; width: 340px; height: 46px;
    font-size: 20px;
    font-weight: 700;
    letter-spacing: 0.5px;
    text-transform: uppercase;
  }
  .person-role {
    left: 80px; top: 76px; width: 170px; height: 56px;
    font-size: 11px;
    font-weight: 500;
    color: var(--ink-soft);
    text-transform: uppercase;
  }
  .person-phone {
    left: 250px; top: 76px; width: 170px; height: 56px;
    font-size: 12px;
    font-weight: 500;
    color: var(--ink-soft);
  }
  .contact-online {
    left: 80px; top: 132px; width: 340px; height: 56px;
    flex-direction: column;
    font-size: 11.5px;
    font-weight: 500;
    line-height: 1.25;
    color: var(--ink-soft);
  }
  .contact-post {
    left: 80px; top: 188px; width: 340px; height: 52px;
    font-size: 12px;
    font-weight: 500;
    color: var(--ink-soft);
  }
</style>
</head>
<body>
<main class="stage">
  <section class="card card-front" aria-label="Business card front">
    <div class="brand">
      <p class="brand-name">Veltrane Inquiries</p>
      <span class="brand-dot" aria-hidden="true"></span>
    </div>
  </section>

  <section class="card card-back" aria-label="Business card back">
    <svg class="details-frame" width="500" height="286" viewBox="0 0 500 286" aria-hidden="true">
      <rect x="80.5" y="30.5" width="340" height="210"/>
      <line x1="80" y1="76.5" x2="420" y2="76.5"/>
      <line x1="250.5" y1="76" x2="250.5" y2="132"/>
      <line x1="80" y1="132.5" x2="420" y2="132.5"/>
      <line x1="80" y1="188.5" x2="420" y2="188.5"/>
      <line x1="242" y1="30" x2="254" y2="0"/>
      <line x1="150" y1="240" x2="138" y2="286"/>
    </svg>
    <h1 class="detail person-name">Morgan Kalvane</h1>
    <p class="detail person-role">Founder &amp; CEO</p>
    <p class="detail person-phone">0437862914</p>
    <p class="detail contact-online">
      <span>info@veltraneinquiries.com.au</span>
      <span>www.veltraneinquiries.com.au</span>
    </p>
    <p class="detail contact-post">PO Box 48, Birchwood NSW 2301</p>
  </section>
</main>
</body>
</html>
```